Policy Manual in Education

I need the attached document to be put in a publishable format, with graphics a professional layout, and something that looks more like a professional report, etc. Use color samples from http://www.brwt-qx.com/ and www.kv7lo.com, my company is Kv7lo, we were hired to write the report and we also built the BRWT resource center http://www.brwt-qx.com/ .

Target Market(s)

Education

Requirements
Must have
• Look and feel around NM. http://www.brwt-qx.com/ and www.kv7lo.com

```html
<!DOCTYPE html>
<html lang="en">
<head>
<meta charset="utf-8">
<title>Policy Manual in Education – Page Spreads</title>
<link href="https://fonts.googleapis.com/css2?family=Lato:wght@300;400;700;900&family=Open+Sans:wght@400;600;700&display=swap" rel="stylesheet">
<style>
:root{
  --navy:#153e75;
  --navy-deep:#0f2e5c;
  --blue:#1f5fa8;
  --link:#2a6cc4;
  --orange:#f6a21a;
  --orange-deep:#ee8a12;
  --ink:#2b2b2b;
  --grey-bg:#b4b4b4;
  --rule:#9bb3d1;
  --row:#dde7f3;
  --white:#ffffff;
}
*{box-sizing:border-box;margin:0;padding:0}
html,body{width:1200px;height:1200px;overflow:hidden;background:var(--grey-bg)}
body{position:relative;font-family:"Open Sans",Arial,sans-serif;color:var(--ink)}
.page{position:absolute;width:260px;height:350px;background:var(--white);overflow:hidden;box-shadow:0 1px 3px rgba(0,0,0,.18)}
.col-1{left:54px}.col-2{left:458px}.col-3{left:862px}
.row-1{top:32px}.row-2{top:426px}.row-3{top:819px}

.job-meta{position:absolute;right:22px;top:12px;font-size:2.6px;line-height:3.4px;text-align:right;color:#555}
.page-title{position:absolute;left:30px;right:22px;top:25px;text-align:center;font-family:"Lato",sans-serif;font-weight:400;font-size:8.6px;letter-spacing:.3px;color:#222;border-bottom:.7px solid var(--rule);padding-bottom:2px}
.body{position:absolute;font-size:3.5px;line-height:5px;color:var(--ink)}
.body p{margin-bottom:3.5px}
.lead{color:var(--link)}
.accent{color:var(--link)}
.sub{font-family:"Lato",sans-serif;font-weight:700;color:var(--blue);font-size:6.4px;line-height:8px;margin:4px 0 1px}
.kicker{color:var(--link);font-size:3.6px;margin-bottom:1px}
.photo{position:absolute;background:linear-gradient(135deg,#3a4350 0%,#6b6a66 45%,#2c3038 100%)}
.photo.warm{background:linear-gradient(135deg,#4b5360 0%,#8a6f57 50%,#2d323a 100%)}

.footer{position:absolute;left:0;right:0;bottom:7px;height:7px}
.footer .bar{position:absolute;left:0;top:1px;width:170px;height:5px;background:var(--navy);clip-path:polygon(0 0,100% 0,96% 100%,0 100%)}
.footer .url{position:absolute;left:20px;top:2px;font-size:2.8px;color:#fff;font-weight:600}
.footer .mark{position:absolute;left:186px;top:-1px;font-family:"Lato",sans-serif;font-weight:900;font-size:7px;line-height:7px;color:var(--orange-deep)}
.footer .num{position:absolute;right:0;top:1px;width:42px;height:5px;background:var(--orange);clip-path:polygon(8% 0,100% 0,100% 100%,0 100%);font-size:3.6px;line-height:5px;text-align:center;color:var(--navy-deep)}

.cover-art{position:absolute;inset:0}
.brand{position:absolute;font-family:"Lato",sans-serif;font-weight:900;color:var(--orange-deep)}
.brand small{display:block;font-weight:700;color:var(--navy-deep)}

table{border-collapse:separate;border-spacing:1.5px;width:100%;font-size:3px}
th{background:var(--blue);color:#fff;font-weight:600;height:5px;line-height:5px;padding:0 3px}
td{background:var(--row);height:5.2px;line-height:5.2px;padding:0 3px}
td.num{text-align:center}
tr.phase td{color:var(--link);font-weight:700}
tr.total td{background:#6aa7e0;color:#fff;font-weight:700}

.callout{position:absolute;left:34px;right:28px;top:44px;height:22px;background:var(--navy)}
.callout .icon{position:absolute;left:0;top:0;width:22px;height:22px;background:var(--orange)}
.callout p{position:absolute;left:26px;right:6px;top:4px;font-size:3.6px;line-height:4.6px;color:#fff}

.toc-head{font-family:"Lato",sans-serif;font-weight:700;color:var(--blue);font-size:6.8px;margin-bottom:5px}
.toc-row{display:flex;align-items:baseline;font-size:3.4px;line-height:5.6px}
.toc-row .dots{flex:1;border-bottom:.5px dotted #777;margin:0 3px}

.bullets{list-style:none}
.bullets li{padding-left:3px}
.bullets li::before{content:"\25A0";color:var(--navy);font-size:2.6px;margin-right:1.5px}
.arrows{list-style:none;padding-left:30px}
.arrows li{color:var(--link)}
.arrows li::before{content:"\25B6";font-size:2.6px;margin-right:1.5px}

.contact{position:absolute;left:128px;top:324px;font-size:2.6px;line-height:3.6px;color:var(--navy-deep)}
.contact span::before{content:"";display:inline-block;width:3px;height:3px;border-radius:50%;background:var(--navy);margin-right:2px;vertical-align:-.3px}
.address{position:absolute;left:186px;top:324px;font-size:2.6px;line-height:3.6px;color:var(--navy-deep);border-left:.5px solid #999;padding-left:3px}
</style>
</head>
<body>

<!-- Front cover -->
<section class="page col-1 row-1 cover">
  <svg class="cover-art" viewBox="0 0 260 350" width="260" height="350" role="img" aria-label="Blue cover panel with faint triangle motif and orange diagonal band">
    <defs>
      <linearGradient id="coverBlue" x1="0" y1="0" x2="0" y2="1">
        <stop offset="0" stop-color="#1b5aa0"/>
        <stop offset="1" stop-color="#0f2e5c"/>
      </linearGradient>
      <linearGradient id="coverOrange" x1="0" y1="0" x2="1" y2="0">
        <stop offset="0" stop-color="#f7b12a"/>
        <stop offset="1" stop-color="#f08a12"/>
      </linearGradient>
    </defs>
    <polygon points="0,0 260,0 260,212 0,286" fill="url(#coverBlue)"/>
    <polygon points="0,286 260,212 260,238 0,300" fill="url(#coverOrange)"/>
  </svg>
  <div class="brand" style="left:118px;top:288px;font-size:21px;line-height:20px;">ALTORA<small style="font-size:6px;line-height:7px;">Public Learning Office</small></div>
</section>

<!-- Page 8 -->
<section class="page col-2 row-1">
  <div class="job-meta">Job No. - Engineering Report<br>Date: 2 July 2018</div>
  <h2 class="page-title">HEADLINE HERE</h2>
  <div class="photo" style="left:27px;top:44px;width:91px;height:130px" role="img" aria-label="Photo of a stressed businessman at his desk"></div>
  <div class="photo warm" style="left:27px;top:197px;width:91px;height:116px" role="img" aria-label="Photo of a colleague comforting a tired office worker"></div>
  <div class="body" style="left:131px;top:44px;width:104px">
    <p class="lead">Tallywise's mission is to help and support the self-employed and small business owners with their administrative tasks so they can focus on what matters – their business.</p>
    <p>Administrative tasks are cumbersome, time-consuming and often prevent small owners from focusing their time and energy on their business and their customers. They can also be extremely stressful and nerve-wracking for those attempting these tasks for the first time.</p>
    <p>At Tallywise, we envisage accounting for the self-employed and small business owners as being <span class="accent">automated and decentralized</span>.</p>
    <p>Accounting can and should be done automatically. By connecting to all sources of accounting data such as bank accounts, payment systems, e-commerce websites, and invoicing systems, Tallywise AI automatically completes these tasks, which would take hours to do manually. Bookings are created automatically and fully completed. Financial statements are available within a couple of clicks, and after analysing your data, Tallywise AI will offer you tips to improve your financial stability.</p>
    <p>What may seem like a pipedream to the millions of self-employed who struggle with</p>
    <div class="sub">The Tallywise model</div>
    <p>Tallywise is based on an innovative license model that uses Token-as-a-License (TaaL). The token represents lifelong software license for Tallywise solutions. The Pre-ICO token sales will enable Tallywise to complete its development of Tallywise AI to deliver fully automatic bookkeeping.</p>
  </div>
  <div class="footer"><div class="bar"></div><div class="url">www.website.com</div><div class="mark">ALTORA</div><div class="num">8</div></div>
</section>

<!-- Page 2 -->
<section class="page col-3 row-1">
  <div class="job-meta">Job No. - Engineering Report<br>Date: 2 July 2018</div>
  <h2 class="page-title">HEADLINE HERE</h2>
  <div class="body" style="left:34px;top:48px;width:200px">
    <div class="sub">Solution</div>
    <div class="kicker">AI automated accounting</div>
    <p>Tallywise builds automation in stages on top of its current system to reach full automation thanks to the Tallywise AI. Tallywise AI automates every manual task performed by the user. It starts by connecting to all sources of accounting data such as bank accounts, credit card, webshop or document management systems. Based on these data, Tallywise AI creates bookings and generates financial reports. Finally, Tallywise AI features chat-like interface that allows users to communicate seamlessly with it, viewing it as a trusted advisor over time for all their accounting queries.</p>
    <div class="kicker">Blockchain software license or Token-as-a-License (TaaL)</div>
    <p>It is possible to create tokens on blockchain that represent software licenses, also known as Token-as-a-Licence (TaaL). Tallywise creates TaaL by using the Nimbus official wallet which interacts with the Nimbus blockchain. Upon purchase of TaaL, the token holder is free to transfer or sell TaaL using secondary market that is built directly over the blockchain, in our case, the Nimbus marketplace. Tallywise checks the validity of a token against the blockchain ensuring that token holders have access to the software. TaaL make distribution and securisation of software licenses easier for software developers. It also makes the management and resale of software license easier for software owners. All in all, TaaL has a higher value as a normal software license.</p>
    <div class="sub">Pre-ICO Token sale</div>
    <p>To realize this innovative vision, Tallywise is launching a pre-ICO in form of a token sale on Nimbus blockchain. 20,000,000 tokens are available to purchase for the price of CHF 0.10 each during a 30-day period to be announced. Tokens represent Tallywise lifelong software licenses and by purchasing enough tokens, holders gain access to Tallywise software: 15,000 tokens give access to Tallywise invoicing or accounting. 20,000 tokens give access to both Tallywise accounting and invoicing. Future customers will still have the opportunity to buy directly yearly or monthly subscriptions to have access to Tallywise.</p>
    <div class="sub">Future plans</div>
    <p>A future ICO is planned between 18 and 24 months after the pre-ICO token sale. This offering will support the development of Tallywise into a fully decentralized, privacy-focused ecosystem of applications. The new model will reward each participant so that a new world with zero administrative tasks becomes reality.</p>
  </div>
  <div class="footer"><div class="bar"></div><div class="url">www.website.com</div><div class="mark">ALTORA</div><div class="num">2</div></div>
</section>

<!-- Page 7 -->
<section class="page col-1 row-2">
  <div class="job-meta">Job No. - Engineering Report<br>Date: 2 July 2018</div>
  <h2 class="page-title">HEADLINE HERE</h2>
  <div class="photo" style="left:30px;top:44px;width:210px;height:88px" role="img" aria-label="Photo of a stressed businessman being comforted in an office"></div>
  <div class="body" style="left:27px;top:139px;width:214px">
    <p class="lead">Tallywise's mission is to help and support the self-employed and small business owners with their administrative tasks so they can focus on what matters – their business.</p>
    <p>Administrative tasks are cumbersome, time-consuming and often prevent small owners from focusing their time and energy on their business and their customers. They can also be extremely stressful and nerve-wracking for those attempting these tasks for the first time.</p>
    <p>At Tallywise, we envisage accounting for the self-employed and small business owners as being <span class="accent">automated and decentralized</span></p>
    <p>Accounting can and should be done automatically. By connecting to all sources of accounting data such as bank accounts, payment systems, e-commerce websites, and invoicing systems, Tallywise AI automatically completes these tasks, which would take hours to do manually. Bookings are created automatically and fully completed. Financial statements are available within a couple of clicks, and after analysing your data, Tallywise AI will offer you tips to improve your financial stability.</p>
    <p>What may seem like a pipedream to the millions of self-employed who struggle with their admin, is already a reality. Now is the time to join Tallywise on its mission to transform the world of bookkeeping through the power of AI</p>
    <div class="sub">The Tallywise model</div>
    <p>Tallywise is based on an innovative license model that uses Token-as-a-License (TaaL). The token represents lifelong software license for Tallywise solutions. The Pre-ICO token sales will enable Tallywise to complete its development of Tallywise AI to deliver fully automatic bookkeeping.</p>
    <p>with leading edge business data access to ensure you have the best available data at your fingertips.</p>
  </div>
  <div class="footer"><div class="bar"></div><div class="url">www.website.com</div><div class="mark">ALTORA</div><div class="num">7</div></div>
</section>

<!-- Page 5 -->
<section class="page col-2 row-2">
  <div class="job-meta">Job No. - Engineering Report<br>Date: 2 July 2018</div>
  <h2 class="page-title">BUDGET AND TIMEFRAME</h2>
  <div class="body" style="left:29px;top:43px;width:210px">
    <div class="sub" style="margin-top:0">Implementation Estimate</div>
    <p>The bulk of the implementation costs will be defined by discovery. Based on similar CRM implementation projects, we feel expect that the CRM side will be something fall between 200 and 300 hours, give or take. The wide swing in hours in phase one is related to the under-defined nature of both the integration needs and our role in the integration project. Our focus in discovery will be to nail down those requirements and our role as it relates to what is needed to integrate the sites with the CRM.</p>
    <table style="margin-top:4px">
      <tr><th style="width:55%">Task</th><th>Hours</th><th>Cost</th></tr>
      <tr><td>Discovery</td><td class="num">40</td><td class="num">$8,000</td></tr>
      <tr class="phase"><td>Phase 1</td><td></td><td></td></tr>
      <tr><td>Discovery</td><td class="num">20-40</td><td class="num">$8,000</td></tr>
      <tr><td>Discovery</td><td class="num">20-40</td><td class="num">$8,000</td></tr>
      <tr><td>Discovery</td><td class="num">20-40</td><td class="num">$8,000</td></tr>
      <tr><td>Total Phase 1</td><td class="num">80-240</td><td class="num">$16,800-40,000</td></tr>
      <tr class="phase"><td>Phase 2</td><td></td><td></td></tr>
      <tr><td>Discovery</td><td class="num">20-40</td><td class="num">$8,000</td></tr>
      <tr><td>Total Phase 2</td><td class="num">80-240</td><td class="num">$16,800-40,000</td></tr>
      <tr class="total"><td>Total Estimated Implementation Cost</td><td class="num">220-480</td><td class="num">$44,000-96,000</td></tr>
    </table>
    <div class="sub" style="margin-top:8px">Project Timeline</div>
    <p>Based on the information we have out our disposal, the March 21st launch date doesn't seem a realistic goal to get both the work done needed to provide the foundation for the future CRM instance and the integration given the state of apparent flux of the requirements. That said, we feel it prudent to proceed with discovery before committing to or pushing that date. We are currently estimating that the first phase will take somewhere between 7 and 12 weeks (including discovery) to complete.</p>
    <table>
      <tr><th style="width:60%">Task</th><th>Weeks to Complete</th></tr>
      <tr><td>Discovery</td><td class="num">1-2</td></tr>
      <tr><td>Phase 1</td><td class="num">6-10</td></tr>
      <tr><td>Phase 2</td><td class="num">8-12</td></tr>
      <tr><td>Total Number of Weeks</td><td></td></tr>
    </table>
  </div>
  <div class="footer"><div class="bar"></div><div class="url">www.website.com</div><div class="mark">ALTORA</div><div class="num">5</div></div>
</section>

<!-- Page 3 -->
<section class="page col-3 row-2">
  <div class="job-meta">Job No. - Engineering Report<br>Date: 2 July 2018</div>
  <h2 class="page-title">VISION</h2>
  <div class="callout">
    <svg class="icon" viewBox="0 0 22 22" width="22" height="22" aria-hidden="true">
      <rect width="22" height="22" fill="#f6a21a"/>
      <circle cx="11" cy="11" r="7" fill="none" stroke="#fff" stroke-width="1.3"/>
      <circle cx="11" cy="11" r="4.2" fill="none" stroke="#fff" stroke-width="1.3"/>
      <circle cx="11" cy="11" r="1.6" fill="#fff"/>
    </svg>
    <p>Tallywise's mission is to help and support the self-employed and small business owners with their administrative tasks so they can focus on what matters – their business.</p>
  </div>
  <div class="body" style="left:34px;top:76px;width:200px">
    <p class="lead">Administrative tasks are cumbersome, time-consuming and often prevent small owners from focusing their time on their business and their customers. They can also be extremely stressful and nerve-wracking for those attempting these tasks for the first time.</p>
    <p style="text-align:center">At Tallywise, we envisage accounting for the self-employed and small business owners as being <span class="accent">automated and decentralized</span></p>
    <p>Accounting can and should be done automatically. By connecting to all sources of accounting data such as bank accounts, payment systems, e-commerce websites, and invoicing systems, Tallywise AI automatically completes these tasks, which would take hours to do manually. Bookings are created automatically and fully completed. Financial statements are available within a couple of clicks, and after analysing your data, Tallywise AI will offer you tips to improve your financial stability.</p>
    <p>What may seem like a pipedream to the millions of self-employed who struggle with their admin, is already a reality. Now is the time to join Tallywise on its mission to transform the world of bookkeeping through the power of AI</p>
    <div class="sub">The Tallywise model</div>
    <p>Tallywise is based on an innovative license model that uses Token-as-a-License (TaaL). The token represents lifelong software license for Tallywise solutions. The Pre-ICO token sales will enable Tallywise to complete its development of Tallywise AI to deliver fully automatic bookkeeping.</p>
    <p>The Pre-ICO token sale will also pave the way for a future Tallywise ICO. Tallywise will launch accounting on the blockchain and ensure your accounting data is comprehensive and private, but available everywhere within your preferred apps. It will empower you to manage your data as you see fit in a fully decentralized way. Furthermore, a new range of business apps will connect to Tallywise to provide you</p>
    <p>with leading edge business data access to ensure you have the best available data at your fingertips.</p>
    <p>Tallywise supports strong data ownership laws that truly protect individuals and ensure they have complete ownership of their data. Through decentralisation Tallywise helps to ensure you always have full ownership of your data to decide how it should be used.</p>
    <p>To find out more about the Tallywise AI project, and the Tallywise TaaL or if you are interested in purchasing Tallywise TaaL, please register with your email at <span class="accent" style="text-decoration:underline">https://www.tallywise.example/ico</span> so we</p>
  </div>
  <div class="footer"><div class="bar"></div><div class="url">www.website.com</div><div class="mark">ALTORA</div><div class="num">3</div></div>
</section>

<!-- Page 6 -->
<section class="page col-1 row-3">
  <div class="job-meta">Job No. - Engineering Report<br>Date: 2 July 2018</div>
  <h2 class="page-title">OUR UNDERSTANDING OF YOUR NEEDS</h2>
  <div class="body" style="left:23px;top:43px;width:218px">
    <p>In the last two weeks of January 2014 we conducted high level conversations both with your staff and your technology partner Signalworks. As a result of those conversations we've been able to gather the following high level goals for your project:</p>
    <p style="font-family:'Lato',sans-serif;font-size:6px;line-height:7px;color:#666">Cloudledger must be in place to support Brightpath at launch and as the program evolves</p>
    <p class="lead" style="font-weight:700">The most critical aspect of this implementation both in terms of time sensitivity as well as functionality is centered around the support for the Brightpath project. Our current understanding of this project and how it relates to Cloudledger is as follows:</p>
    <ul class="bullets">
      <li>Brightpath will be comprised of a series of websites focused on organizing institutions and individuals within six specific community sectors with the goal of increased institutional and public support to help America become better prepared to minimize the risks and maximize opportunities of changing climate.</li>
      <li>The primary goals of the CRM application are:</li>
    </ul>
    <ul class="arrows" style="margin:1px 0 3px">
      <li>capture information of individuals and organizations (along with their respective roles)</li>
      <li>track their progress on their site specific to-do lists and site interactions</li>
      <li>allow GreenCommons to push out next steps (ideally in an automated style) related to their to-do list progress and online interactions</li>
      <li>infuse GreenCommons's online and offline marketing program with useful segmentation information</li>
      <li>natively integrate with both the Brightpath family of sites as well as GreenCommons's email service provider of choice</li>
    </ul>
    <ul class="bullets">
      <li>The data architecture must be well defined but flexible to support the core needs of the sites as launch as well as anticipated needs in the future.</li>
    </ul>
    <ul class="arrows" style="margin:1px 0 3px">
      <li>For instance, the faith based site may collect a "denomination" field, while other sites may not collect that field.</li>
      <li>Future interactions outside of the to-do list may become necessary to track and GreenCommons will need a systemic way to capture those interactions, be able to segment on them and potentially provide automated marketing around those similar to the to-do list</li>
    </ul>
    <ul class="bullets">
      <li>The information collected from the Brightpath sites must be combined with current information held within GreenCommons and provide a holistic view of institutions and individuals.</li>
    </ul>
  </div>
  <div class="footer"><div class="bar"></div><div class="url">www.website.com</div><div class="mark">ALTORA</div><div class="num">6</div></div>
</section>

<!-- Table of contents -->
<section class="page col-2 row-3">
  <h2 class="page-title">TABLE OF CONTENTS</h2>
  <div class="body" style="left:30px;top:50px;width:200px">
    <div class="toc-head">Contents</div>
    <div class="toc-row"><span>Table of Contents</span><span class="dots"></span><span>01</span></div>
    <div class="toc-row"><span>Executive Summary</span><span class="dots"></span><span>02</span></div>
    <div class="toc-row"><span>Our Understanding of Your Needs</span><span class="dots"></span><span>02</span></div>
    <div class="toc-row"><span>Our Recommendations</span><span class="dots"></span><span>03</span></div>
    <div class="toc-row"><span>Our Approach</span><span class="dots"></span><span>05</span></div>
    <div class="toc-row"><span>Budget and Timeframe</span><span class="dots"></span><span>07</span></div>
    <div class="toc-row"><span>Appendix A: About Alder Creek</span><span class="dots"></span><span>10</span></div>
    <div class="toc-row"><span>Appendix B: Selected Client List</span><span class="dots"></span><span>10</span></div>
    <div class="toc-row"><span>Appendix C: Our Capabilities</span><span class="dots"></span><span>11</span></div>
    <div class="toc-row"><span>Appendix D: Our Process</span><span class="dots"></span><span>12</span></div>
  </div>
  <div class="footer"><div class="bar"></div><div class="url">www.website.com</div><div class="mark">ALTORA</div><div class="num">01</div></div>
</section>

<!-- Back cover -->
<section class="page col-3 row-3 cover">
  <svg class="cover-art" viewBox="0 0 260 350" width="260" height="350" role="img" aria-label="Blue back cover panel with faint triangle motif and orange diagonal band">
    <defs>
      <linearGradient id="backBlue" x1="0" y1="0" x2="0" y2="1">
        <stop offset="0" stop-color="#1b5aa0"/>
        <stop offset="1" stop-color="#0f2e5c"/>
      </linearGradient>
      <linearGradient id="backOrange" x1="0" y1="0" x2="1" y2="0">
        <stop offset="0" stop-color="#f7b12a"/>
        <stop offset="1" stop-color="#f08a12"/>
      </linearGradient>
    </defs>
    <polygon points="0,0 260,0 260,188 0,280" fill="url(#backBlue)"/>
    <polygon points="0,280 260,188 260,212 0,293" fill="url(#backOrange)"/>
  </svg>
  <div class="brand" style="left:46px;top:304px;font-size:10px;line-height:10px;">ALTORA<small style="font-size:3px;line-height:4px;">Public Learning Office</small></div>
  <div class="contact" style="left:102px;top:304px">
    <span>000-318-4470 Ext 101</span><br>
    <span>hello@altora-learn.example</span><br>
    <span>www.altora-learn.example</span>
  </div>
  <div class="address" style="left:154px;top:304px">210, 88 Harbour Lane<br>Eastbay District, Region 4 0X1</div>
</section>

</body>
</html>
```